Need a Brochure Design

We need a brochure designed (A4 two sides or A3 foldable which is equal to 2 x A4 = total of four pages )

Brief and Logo attached.

```html
<!DOCTYPE html>
<html lang="en">
<head>
<meta charset="UTF-8">
<title>Room Ready Styling – Brochure</title>
<link href="https://fonts.googleapis.com/css2?family=Montserrat:wght@400;500;600&display=swap" rel="stylesheet">
<style>
  :root{
    --backdrop:#58585a;
    --paper:#ffffff;
    --peach:#fbe1cf;
    --ink:#1e1e1e;
    --rule:#2a2a2a;
    --photo-light:#e9e6e2;
    --photo-warm:#d8c7b2;
    --photo-grey:#b9b8b6;
    --voucher-black:#111111;
    --voucher-gold:#c9962a;
  }
  *{margin:0;padding:0;box-sizing:border-box;}
  html,body{width:1200px;height:1200px;overflow:hidden;background:var(--backdrop);}
  body{position:relative;font-family:"Montserrat",sans-serif;color:var(--ink);}
  .page{position:absolute;top:239px;width:557px;height:717px;background:var(--paper);overflow:hidden;}
  .page--front{left:40px;}
  .page--back{left:618px;}
  .abs{position:absolute;}
  .photo{position:absolute;}
  p,li{font-size:10.4px;line-height:12.8px;}

  /* front */
  .intro-band{left:0;top:0;width:557px;height:151px;background:var(--peach);}
  .intro-text{left:19px;top:24px;width:380px;}
  .intro-text p{margin-bottom:8.5px;}
  .portrait{left:410px;top:16px;width:126px;height:128px;background:linear-gradient(180deg,#d9d9d9,#c4c4c4 60%,#e8e6e3);}
  .team-photo{left:0;top:159px;width:249px;height:207px;background:linear-gradient(135deg,#dcdcdc,#cfcac3 55%,#8a6a45);}
  .impressions{left:261px;top:161px;width:285px;}
  .impressions h2{font-size:16px;font-weight:500;line-height:19px;margin-bottom:2px;}
  .impressions p{margin-bottom:12.5px;}
  .why{left:17px;top:380px;width:240px;}
  .why h3{font-size:11.8px;font-weight:600;margin-bottom:10px;}
  .why ul{list-style:none;}
  .why li{font-size:10.4px;line-height:21.2px;padding-left:3px;}
  .why li::before{content:"\2022";margin-right:3px;}
  .dining-photo{left:259px;top:383px;width:298px;height:164px;background:linear-gradient(135deg,#f1ede8,#e4d9c9 55%,#c9b59a);}
  .referrals{left:22px;top:541px;width:224px;text-align:center;font-size:15.5px;font-weight:600;}
  .voucher{left:22px;top:568px;width:224px;height:131px;background:linear-gradient(135deg,var(--voucher-gold) 0%,var(--voucher-black) 30%,var(--voucher-black) 100%);}

  .brand{position:absolute;top:582px;display:flex;align-items:center;gap:6px;font-size:11px;font-weight:500;color:var(--ink);}
  .brand-dot{width:14px;height:14px;border-radius:50%;background:var(--peach);}
  .contact{position:absolute;top:623px;}
  .contact-lead{font-size:10.6px;}
  .contact-list{list-style:none;margin-top:8px;margin-left:16px;}
  .contact-list li{display:flex;align-items:center;gap:12px;font-size:10.6px;line-height:16px;}
  .contact-list svg{width:11px;height:11px;flex:none;}

  /* back */
  .headline-band{left:0;top:0;width:557px;height:68px;background:var(--peach);display:flex;align-items:center;justify-content:center;}
  .headline-band h1{font-size:16px;font-weight:500;line-height:21px;text-align:center;}
  .price{left:26px;width:205px;}
  .price-rule{left:49px;width:146px;height:1px;background:var(--rule);}
  .gallery-1{left:259px;top:71px;width:298px;height:116px;background:linear-gradient(135deg,#ececec,#dcd8d2 60%,#b7a58e);}
  .gallery-2{left:259px;top:193px;width:298px;height:118px;background:linear-gradient(135deg,#9b9891,#d9d6d1 50%,#a0583a);}
  .gallery-3{left:259px;top:319px;width:298px;height:117px;background:linear-gradient(135deg,#e6e6e6,#c9a77c 60%,#2b2b2b);}
  .gallery-4{left:259px;top:441px;width:298px;height:117px;background:linear-gradient(135deg,#f0f0f0,#d8d3cb 55%,#5e7a5c);}
  .benefits-box{left:0;top:441px;width:254px;height:276px;background:var(--peach);}
  .benefits{left:21px;top:470px;width:220px;}
  .benefits p{margin-bottom:12.3px;}
</style>
</head>
<body>

<section class="page page--front">
  <div class="abs intro-band"></div>
  <div class="abs intro-text">
    <p>Hey there,</p>
    <p>I’m Mara, Owner and Creative Director of Room Ready Styling. Please let me introduce you to our amazingly creative property styling team!</p>
    <p>We are a friendly bunch who are passionate about home staging. We’ve been property staging apartments, townhouses, and standalone homes since 2009. An all-female powerhouse, we combine our experience in art, interior design, retail, and business to offer professional home styling throughout Melbourne.</p>
  </div>
  <div class="photo portrait" role="img" aria-label="Portrait of the creative director in a white blouse"></div>

  <div class="photo team-photo" role="img" aria-label="The styling team posed around a mustard armchair"></div>
  <div class="abs impressions">
    <h2>Because first impressions count</h2>
    <p>A gorgeous looking home sells faster and fetches a higher price.</p>
    <p>At RoomReadyStyling, we help our property clients create a lasting impression with minimal spend. Our property vendors are usually looking for home-staging on a tight budget. They come to us searching for creativetransformations to help them sell well. Thoughtfully positioned furniture and on-trend interior décor can make all the difference!</p>
    <p>Our property styling service includes a free consultation, longer rental periods, and installation and removal.</p>
  </div>

  <div class="abs why">
    <h3>Why choose RoomReadyStyling?</h3>
    <ul>
      <li>Experienced, enthusiastic property stylists</li>
      <li>Work with low client budgets</li>
      <li>Fast turnaround to a tight deadline</li>
      <li>Flexible rental terms(4/6/8 weeks)</li>
      <li>Happy to recommend potential customers</li>
    </ul>
  </div>
  <div class="photo dining-photo" role="img" aria-label="Staged dining room with timber table and white chairs"></div>

  <div class="abs referrals">We Reward Referrals !</div>
  <div class="photo voucher" role="img" aria-label="Black and gold gift voucher: $200 for every successful referral"></div>

  <div class="brand" style="left:318px;"><span class="brand-dot"></span>Room Ready Styling</div>
  <div class="contact" style="left:273px;">
    <p class="contact-lead">We’d love to hear from you, so please contact us</p>
    <ul class="contact-list">
      <li><svg viewBox="0 0 12 12"><circle cx="6" cy="6" r="5.3" fill="none" stroke="#1e1e1e" stroke-width="0.9"/><path d="M4 3.3l1 1.1-.5.8c.4.9 1 1.5 1.9 1.9l.8-.5 1.1 1-.6 1c-2.3-.3-4-2-4.3-4.3z" fill="#1e1e1e"/></svg>0400 123 456</li>
      <li><svg viewBox="0 0 12 12"><rect x="1" y="2.5" width="10" height="7" fill="#1e1e1e"/><path d="M1 2.5l5 4 5-4" fill="none" stroke="#fff" stroke-width="0.9"/></svg>hello@roomreadystyling.com.au</li>
      <li><svg viewBox="0 0 12 12" fill="none" stroke="#1e1e1e" stroke-width="0.9"><circle cx="6" cy="6" r="5"/><ellipse cx="6" cy="6" rx="2.2" ry="5"/><path d="M1 6h10M2 3.5h8M2 8.5h8"/></svg>www.roomreadystyling.com.au</li>
    </ul>
  </div>
</section>

<section class="page page--back">
  <div class="abs headline-band">
    <h1>We average over 185 property styling projects per year, with a<br>large proportion selling in less than 30 days!</h1>
  </div>

  <p class="abs price" style="top:87px;">1 Bedroom Property - Full Styling + 6 Weeks Free Hire* - $1,897.00 Original Price:2,750.00</p>
  <div class="abs price-rule" style="top:145px;"></div>
  <p class="abs price" style="top:180px;">2 Bedroom Property - Full Styling + 6 Weeks Free Hire - $2,697.00 Original Price:3,250.00</p>
  <div class="abs price-rule" style="top:240px;"></div>
  <p class="abs price" style="top:272px;">3 Bedroom Property - Full Styling + 6 Weeks Free Hire* - $2,997.00 Original Price:4,470.00</p>
  <div class="abs price-rule" style="top:335px;"></div>
  <p class="abs price" style="top:362px;">4 Bedroom Property - Full Styling + 6 Weeks Free Hire - $3,897.00 Original Price:5,485.00</p>

  <div class="photo gallery-1" role="img" aria-label="Open-plan living room and kitchen, styled"></div>
  <div class="photo gallery-2" role="img" aria-label="Outdoor courtyard with lounge setting and timber screen"></div>
  <div class="photo gallery-3" role="img" aria-label="Dining table with black chairs beside kitchen bench"></div>
  <div class="photo gallery-4" role="img" aria-label="Apartment lounge with sofa, armchair and indoor plant"></div>

  <div class="abs benefits-box"></div>
  <div class="abs benefits">
    <p>Helping your property reach its highest potential without busting the budget.</p>
    <p>Achieving a record number of viewings and the highest possible sale price.</p>
    <p>Installation, interior design and decoration, and removal included.</p>
    <p>Pre-sale home preparation to post-sale removal.</p>
    <p>Free consultation and longer rental periods.</p>
    <p>A small investment for such a large transformation!</p>
  </div>

  <div class="brand" style="left:336px;"><span class="brand-dot"></span>Room Ready Styling</div>
  <div class="contact" style="left:274px;">
    <p class="contact-lead">We’d love to hear from you, so please contact us</p>
    <ul class="contact-list">
      <li><svg viewBox="0 0 12 12"><circle cx="6" cy="6" r="5.3" fill="none" stroke="#1e1e1e" stroke-width="0.9"/><path d="M4 3.3l1 1.1-.5.8c.4.9 1 1.5 1.9 1.9l.8-.5 1.1 1-.6 1c-2.3-.3-4-2-4.3-4.3z" fill="#1e1e1e"/></svg>0400 123 456</li>
      <li><svg viewBox="0 0 12 12"><rect x="1" y="2.5" width="10" height="7" fill="#1e1e1e"/><path d="M1 2.5l5 4 5-4" fill="none" stroke="#fff" stroke-width="0.9"/></svg>hello@roomreadystyling.com.au</li>
      <li><svg viewBox="0 0 12 12" fill="none" stroke="#1e1e1e" stroke-width="0.9"><circle cx="6" cy="6" r="5"/><ellipse cx="6" cy="6" rx="2.2" ry="5"/><path d="M1 6h10M2 3.5h8M2 8.5h8"/></svg>www.roomreadystyling.com.au</li>
    </ul>
  </div>
</section>

</body>
</html>
```